Business Card Design

Non-profit organization creating opportunities for:
Personal empowerment
Community Outreach
Healthier Life Choices
Body/Mind/Spirit Nourishment
Emotional Transformation
Charity & Network Opportunities
Everyday people making An extrodinary sufferance
All achieved from the Source within YOU.
Organization logo is the ying yang symbol with a small circle above it as if it were the head and the ying yang symbol was the body.  Also in side upper ying needs to be a heart and in the lower yang needs to be the letter C. This is very important as it came to me in a dream n the forming of this organization.  Color choice is open although a thought I hade was that the heart is red metallic foil (sine a red heart is the symbol of love)and the c is gold foil( the gifts of the 3 wise men and gold being one of them).a verticle card is preferred and logo as large as possible on it even if ying yang is made oval Ilook forward to the layouts and designs you can come up with.

Contact Information for Business Card
Lumen Harbor. Org
Paul Marsky
Executive Director
Lumen harbor.paul@brindlemail.com
512-394-2086

```html
<!DOCTYPE html>
<html lang="en">
<head>
<meta charset="utf-8">
<title>Lumen Harbor — Business Card</title>
<link href="https://fonts.googleapis.com/css2?family=Lato:wght@400;700&display=swap" rel="stylesheet">
<style>
  :root {
    --backdrop: #e2e2e2;
    --card-light: #f7f7f5;
    --card-dark: #2f2f2f;
    --ink: #2b2b2b;
    --accent-red: #d9262b;
    --accent-gold: #c9a55a;
    --paper-white: #f4f4f2;
  }
  * { margin: 0; padding: 0; box-sizing: border-box; }
  html, body {
    width: 1200px;
    height: 747px;
    overflow: hidden;
    background: var(--backdrop);
    font-family: 'Lato', sans-serif;
  }
  .stage {
    width: 1200px;
    height: 747px;
    display: flex;
    justify-content: center;
    align-items: center;
    gap: 40px;
  }
  .card {
    width: 356px;
    height: 622px;
    border-radius: 3px;
    box-shadow: 0 6px 18px rgba(0,0,0,0.18);
    position: relative;
  }
  .card--front {
    background: var(--card-light);
    color: var(--ink);
  }
  .card--back {
    background: var(--card-dark);
    color: var(--paper-white);
  }
  .brand {
    position: absolute;
    left: 0;
    right: 0;
    display: flex;
    justify-content: center;
    align-items: center;
    gap: 10px;
    font-weight: 700;
    letter-spacing: 0.04em;
  }
  .brand__dot {
    border-radius: 50%;
    background: var(--accent-gold);
    flex: none;
  }
  .card--front .brand {
    top: 118px;
    font-size: 20px;
    color: var(--ink);
  }
  .card--front .brand__dot { width: 14px; height: 14px; }
  .card--back .brand {
    top: 285px;
    font-size: 36px;
    color: var(--paper-white);
  }
  .card--back .brand__dot { width: 26px; height: 26px; }
  .identity {
    position: absolute;
    top: 318px;
    left: 0;
    right: 0;
    text-align: center;
  }
  .identity__name {
    font-size: 24px;
    font-weight: 700;
    text-transform: uppercase;
    letter-spacing: 0.06em;
  }
  .identity__title {
    font-size: 22px;
    font-weight: 400;
    margin-top: 2px;
  }
  .divider {
    position: absolute;
    top: 412px;
    left: 73px;
    width: 210px;
    height: 2px;
    background: var(--accent-red);
  }
  .contact {
    position: absolute;
    top: 452px;
    left: 0;
    right: 0;
    text-align: center;
    font-size: 19px;
    line-height: 1.4;
  }
  .contact__org { font-weight: 700; }
  .contact__email { font-size: 17px; }
</style>
</head>
<body>
  <main class="stage">
    <section class="card card--front">
      <div class="brand"><span class="brand__dot"></span>Lumen Harbor</div>
      <div class="identity">
        <p class="identity__name">Paul Marsky</p>
        <p class="identity__title">Executive Director</p>
      </div>
      <div class="divider"></div>
      <div class="contact">
        <p class="contact__org">Lumen Harbor. Org</p>
        <p class="contact__phone">512-394-2086</p>
        <p class="contact__email">Lumen harbor.paul@brindlemail.com</p>
      </div>
    </section>
    <section class="card card--back">
      <div class="brand"><span class="brand__dot"></span>Lumen Harbor</div>
    </section>
  </main>
</body>
</html>
```